Robotic startup business cards

We are looking for a design for a set of business cards which reflect the spirit and humor of Torvexa Robotics. We want to present ourselves as sleek, professional, but laid-back consulting company.

We primarily focus on developing robotic arms software. This software controls robots and does things like grab items, pick objects up, move them, etc.

We want to allow you maximum design creativity, but do ask that you consider our existing style guidelines (see attached files) in order to make our brand cohesive.

Target Market(s)

Startups and Mid-size robotic companies

Industry/Entity Type

Business

Contact Information for Business Card

Liam Brantly, PhD
Roboticist | Torvexa Consulting | 318.572.6094

Font styles to use
Other font styles liked:
• Source code pro

Requirements
Must have
• robots or robotic arms
• similar color scheme that works with existing brand guidelines
Nice to have
• please consider our existing style guidelines (see attached files) in order to make our brand cohesive.
• minimalism style is generally nice.
Should not have
• An old, boring, or corporate feel. Too much text.

```html
<!DOCTYPE html>
<html lang="en">
<head>
<meta charset="utf-8">
<title>Torvexa Robotics – Business Cards</title>
<link rel="stylesheet" href="https://fonts.googleapis.com/css2?family=Source+Code+Pro:wght@400;500;700&display=swap">
<style>
  :root {
    --bg: #e6e8ea;
    --card-dark: #000000;
    --card-light: #ffffff;
    --brand-green: #2fe28c;
    --ink: #111111;
    --ink-soft: #333333;
    --on-dark: #ffffff;
  }
  * { box-sizing: border-box; margin: 0; padding: 0; }
  html, body {
    width: 1200px; height: 758px; overflow: hidden;
    background: var(--bg);
    font-family: "Source Code Pro", monospace;
  }
  .canvas { position: relative; width: 1200px; height: 758px; }

  .card {
    position: absolute;
    width: 520px; height: 300px;
    border-radius: 22px;
    box-shadow: 0 14px 30px rgba(0,0,0,0.18);
    overflow: hidden;
  }

  /* Back of card */
  .card--back {
    left: 60px; top: 110px;
    background: var(--card-dark);
    color: var(--on-dark);
  }
  .card--back .brand-name {
    position: absolute; left: 0; right: 0; top: 100px;
    text-align: center;
    font-size: 48px; font-weight: 700; letter-spacing: 0.08em;
    color: var(--brand-green);
  }
  .card--back .tagline {
    position: absolute; left: 0; right: 0; bottom: 48px;
    text-align: center;
    font-size: 11px; font-weight: 500; letter-spacing: 0.12em;
    color: var(--on-dark);
  }

  /* Front of card */
  .card--front {
    left: 620px; top: 350px;
    background: var(--card-light);
    color: var(--ink);
  }
  .brand-lockup {
    position: absolute; left: 36px; top: 48px;
    display: flex; align-items: center; gap: 16px;
  }
  .brand-lockup .brand-square {
    width: 36px; height: 36px;
    background: var(--brand-green);
    border-radius: 4px;
  }
  .brand-lockup .brand-words {
    font-size: 26px; font-weight: 400; letter-spacing: 0.2em;
    line-height: 1.05; color: var(--ink);
  }
  .brand-lockup .brand-words small {
    display: block; font-size: 13px; letter-spacing: 0.38em;
  }

  .person {
    position: absolute; left: 36px; bottom: 46px;
  }
  .person .name {
    font-size: 20px; font-weight: 700; letter-spacing: 0.02em;
  }
  .person .role {
    font-size: 13px; font-weight: 500; color: var(--ink-soft);
  }

  .contact {
    position: absolute; right: 36px; bottom: 44px;
    list-style: none;
    display: flex; flex-direction: column; gap: 8px;
  }
  .contact li {
    display: flex; align-items: center; gap: 12px;
    font-size: 12px; font-weight: 500;
  }
  .contact svg {
    width: 14px; height: 14px;
    stroke: var(--brand-green); fill: none; stroke-width: 1.6;
    flex: none;
  }
</style>
</head>
<body>
<main class="canvas">

  <section class="card card--back" aria-label="Card back">
    <div class="brand-name">TORVEXA</div>
    <p class="tagline">ROBOTIC SOFTWARE CONSULTANTS</p>
  </section>

  <section class="card card--front" aria-label="Card front">
    <div class="brand-lockup">
      <span class="brand-square" aria-hidden="true"></span>
      <div class="brand-words">TORVEXA<small>CONSULTING</small></div>
    </div>

    <div class="person">
      <p class="name">LIAM BRANTLY, PhD</p>
      <p class="role">Roboticist</p>
    </div>

    <ul class="contact">
      <li>
        <svg viewBox="0 0 16 16" aria-hidden="true"><path d="M3 2h3l1.5 3.5-2 1.2a8 8 0 0 0 3.8 3.8l1.2-2L14 10v3a1 1 0 0 1-1 1A11 11 0 0 1 2 3a1 1 0 0 1 1-1z"/></svg>
        318.572.6094
      </li>
      <li>
        <svg viewBox="0 0 16 16" aria-hidden="true"><rect x="1.5" y="3.5" width="13" height="9" rx="1"/><path d="M2 4l6 5 6-5"/></svg>
        hello@torvexa.ai
      </li>
      <li>
        <svg viewBox="0 0 16 16" aria-hidden="true"><circle cx="8" cy="8" r="6.2"/><path d="M1.8 8h12.4M8 1.8c2 2 2 10.4 0 12.4M8 1.8c-2 2-2 10.4 0 12.4"/></svg>
        www.torvexa.ai
      </li>
      <li>
        <svg viewBox="0 0 16 16" aria-hidden="true"><circle cx="8" cy="8" r="5.5"/></svg>
        @TorvexaRobotics
      </li>
    </ul>
  </section>

</main>
</body>
</html>
```